Relocation/furniture installation company needs new business cards

we are a relocation and furniture installation company mainly dealing with corporate clients and we are looking for new business card ideas. Cards should incorporate our logo and list our website, phone number and services. The company is only 2 years old but with more staff joining we are in the need for more business cards, so something with an awesome design that is eye catching would go a long way to insure we get our name out there and look good to potential new clients.

Target Market(s)

Corporate

Industry/Entity Type

Trade

Contact Information for Business Card

www.mervoline.co.nz
0508 4 bravok

furniture installation
business relocations
joinery installation
commercial property maintenance

Colors
0592cd
34a7d8
85cae6
85acd3
0356a4
cfdfed
cee9f5
757575
474747

Requirements
Must have
• Business relocations and furniture installation specialists
Nice to have
• something that incorporates our logo.

```html
<!DOCTYPE html>
<html lang="en">
<head>
<meta charset="utf-8">
<title>Mervoline business cards</title>
<link rel="stylesheet" href="https://fonts.googleapis.com/css2?family=PT+Sans:wght@400;700&display=swap">
<style>
  :root {
    --backdrop: #d3dedf;
    --card: #f6f7f9;
    --sky: #4fd0f5;
    --azure: #3ab0f0;
    --stone: #d5dfe0;
    --royal: #1a2bdc;
    --ink: #3b3b3b;
    --ink-soft: #333333;
    --white: #ffffff;
    --shadow: rgba(60, 80, 90, 0.35);
  }
  html, body {
    margin: 0;
    padding: 0;
    width: 1035px;
    height: 1200px;
    overflow: hidden;
    background: var(--backdrop);
  }
  .sheet { display: block; width: 1035px; height: 1200px; }
  .card-face { fill: var(--card); filter: url(#card-shadow); }
  .band-sky { fill: var(--sky); }
  .band-azure { fill: var(--azure); }
  .band-stone { fill: var(--stone); }
  .txt { font-family: "PT Sans", sans-serif; }
  .heading { fill: var(--royal); font-weight: 700; font-size: 29px; }
  .service { fill: var(--ink); font-size: 28px; }
  .web-strip { fill: var(--white); font-weight: 700; font-size: 23px; }
  .person-name { fill: var(--royal); font-weight: 700; font-size: 32px; }
  .person-role { fill: var(--ink-soft); font-size: 21px; }
  .brand-name { fill: var(--royal); font-weight: 700; font-size: 36px; letter-spacing: 2px; }
  .contact { fill: var(--white); font-size: 26px; }
  .clip-icon { fill: none; stroke: var(--ink); stroke-width: 2.2; stroke-linecap: round; }
  .icon-disc { fill: var(--white); }
  .icon-glyph { fill: var(--azure); }
  .icon-line { fill: none; stroke: var(--white); stroke-width: 1.8; }
</style>
</head>
<body>
<svg class="sheet" viewBox="0 0 978 1134" xmlns="http://www.w3.org/2000/svg">
  <defs>
    <filter id="card-shadow" x="-5%" y="-5%" width="115%" height="120%">
      <feDropShadow dx="8" dy="10" stdDeviation="6" flood-color="#3c505a" flood-opacity="0.35"/>
    </filter>
    <symbol id="paperclip" viewBox="0 0 34 34">
      <path class="clip-icon" d="M10 27 L25 10 a4.5 4.5 0 0 0 -6.5 -6.3 L5 19 a7 7 0 0 0 10 9.5 L28 14 M14 22 L23 12"/>
    </symbol>
  </defs>

  <!-- Services card -->
  <g class="card services-card">
    <rect class="card-face" x="93" y="95" width="780" height="443"/>
    <polygon class="band-sky" points="93,95 638,95 692,160 93,160"/>
    <polygon class="band-azure" points="540,95 638,95 692,160 595,160"/>
    <polygon class="band-stone" points="190,470 380,470 440,538 250,538"/>
    <polygon class="band-sky" points="380,470 873,470 873,538 440,538"/>

    <text class="txt heading" x="138" y="213">Specialize</text>
    <use href="#paperclip" x="257" y="243" width="34" height="34"/>
    <text class="txt service" x="308" y="269">Furniture Installation</text>
    <use href="#paperclip" x="257" y="300" width="34" height="34"/>
    <text class="txt service" x="308" y="326">Business Relocations</text>
    <use href="#paperclip" x="257" y="360" width="34" height="34"/>
    <text class="txt service" x="308" y="387">Joinery Installation</text>
    <use href="#paperclip" x="259" y="415" width="34" height="34"/>
    <text class="txt service" x="311" y="442">Commercial Property Maintenance</text>

    <text class="txt web-strip" x="838" y="508" text-anchor="end">www.mervoline.co.nz</text>
  </g>

  <!-- Contact card -->
  <g class="card contact-card">
    <rect class="card-face" x="93" y="604" width="780" height="445"/>
    <polygon class="band-azure" points="558,604 873,604 873,630 580,630"/>
    <polygon class="band-azure" points="93,773 460,773 540,864 93,864"/>
    <polygon class="band-sky" points="93,864 626,864 788,1049 93,1049"/>

    <text class="txt person-name" x="153" y="690">DANIEL VOSS</text>
    <text class="txt person-role" x="153" y="721">Chief Executive Officer</text>

    <text class="txt brand-name" x="717" y="746" text-anchor="middle">MERVOLINE</text>

    <!-- email -->
    <circle class="icon-disc" cx="142" cy="816" r="22"/>
    <rect class="icon-glyph" x="129" y="807" width="26" height="18"/>
    <polyline class="icon-line" points="129,807 142,818 155,807"/>
    <text class="txt contact" x="181" y="823">daniel@mervoline.co.nz</text>

    <!-- web -->
    <circle class="icon-disc" cx="141" cy="912" r="22"/>
    <circle class="icon-glyph" cx="141" cy="912" r="12"/>
    <ellipse class="icon-line" cx="141" cy="912" rx="5" ry="12"/>
    <line class="icon-line" x1="129" y1="912" x2="153" y2="912"/>
    <text class="txt contact" x="184" y="920">www.mervoline.co.nz</text>

    <!-- address -->
    <circle class="icon-disc" cx="142" cy="986" r="22"/>
    <polygon class="icon-glyph" points="128,988 142,975 156,988"/>
    <rect class="icon-glyph" x="132" y="987" width="20" height="12"/>
    <text class="txt contact" x="184" y="981">Tel: +84 91 000 4417</text>
    <text class="txt contact" x="184" y="1020">48 Alder Lane, Kingsford, Victoria 3190</text>
  </g>
</svg>
</body>
</html>
```